Organic lawn care

take the same sign as the mosquito sign, only instead of the mosquito image have the red circle and line cross out the text of "chemicals". Have the sign say "this lawn receives ORGANIC grass treatments" "instantly SAFE for people and pets"

Lawn Care

```html
<!DOCTYPE html>
<html lang="en">
<head>
<meta charset="utf-8">
<title>Organic Lawn Care Yard Sign</title>
<link rel="stylesheet" href="https://fonts.googleapis.com/css2?family=Anton&family=Archivo:wdth,wght@125,900&family=Open+Sans:ital,wght@0,400;1,800&family=Outfit:wght@400;800&family=Roboto+Condensed:wght@700&family=Saira+Condensed:ital,wght@1,800&display=swap">
<style>
  :root {
    --ink: #000000;
    --paper: #ffffff;
    --sky: #4db5f5;
    --lime: #8ff00a;
    --stop-red: #ff1a0f;
  }
  html, body {
    margin: 0;
    padding: 0;
    overflow: hidden;
    background: var(--paper);
  }
  .sign {
    position: relative;
    width: 1200px;
    height: 800px;
    background: var(--paper);
    overflow: hidden;
  }
  .headline {
    position: absolute;
    left: 22px;
    top: 8px;
    margin: 0;
    font-family: "Outfit", sans-serif;
    font-weight: 800;
    font-size: 84px;
    letter-spacing: -1px;
    color: var(--ink);
    line-height: 1;
  }
  .headline .accent { color: var(--lime); }
  .panel {
    position: absolute;
    left: 22px;
    top: 122px;
    width: 1156px;
    height: 520px;
    background: var(--sky);
    border-radius: 32px;
  }
  .organic {
    position: absolute;
    left: 58px;
    top: 126px;
    margin: 0;
    font-family: "Saira Condensed", sans-serif;
    font-style: italic;
    font-weight: 800;
    font-size: 150px;
    letter-spacing: 14px;
    line-height: 1;
    color: var(--paper);
  }
  .grass {
    position: absolute;
    left: 42px;
    top: 262px;
    margin: 0;
    font-family: "Archivo", sans-serif;
    font-stretch: 125%;
    font-weight: 900;
    font-size: 114px;
    letter-spacing: 2px;
    line-height: 1;
    color: var(--lime);
  }
  .treatments, .instantly {
    position: absolute;
    margin: 0;
    font-family: "Open Sans", sans-serif;
    font-weight: 400;
    font-size: 128px;
    letter-spacing: -2px;
    line-height: 1;
    color: var(--ink);
  }
  .treatments { left: 44px; top: 358px; }
  .instantly { left: 64px; top: 478px; }
  .safe {
    position: absolute;
    left: 548px;
    top: 472px;
    margin: 0;
    font-family: "Open Sans", sans-serif;
    font-style: italic;
    font-weight: 800;
    font-size: 150px;
    letter-spacing: -4px;
    line-height: 1;
    color: var(--paper);
  }
  .audience {
    position: absolute;
    left: 894px;
    top: 486px;
    margin: 0;
    font-family: "Roboto Condensed", sans-serif;
    font-weight: 700;
    font-size: 58px;
    line-height: 0.95;
    letter-spacing: -1px;
    color: var(--ink);
  }
  .no-chemicals {
    position: absolute;
    left: 660px;
    top: 60px;
    width: 520px;
    height: 420px;
  }
  .contact {
    position: absolute;
    left: 22px;
    top: 678px;
    margin: 0;
    font-family: "Outfit", sans-serif;
    line-height: 1;
    white-space: nowrap;
  }
  .contact .phone {
    font-weight: 800;
    font-size: 86px;
    letter-spacing: -1px;
    color: var(--sky);
  }
  .contact .web {
    margin-left: 20px;
    font-weight: 400;
    font-size: 88px;
    color: var(--lime);
  }
</style>
</head>
<body>
  <main class="sign">
    <h1 class="headline">This <span class="accent">LAWN</span> Receives</h1>

    <div class="panel"></div>

    <p class="organic">ORGANIC</p>
    <p class="grass">GRASS</p>
    <p class="treatments">Treatments</p>
    <p class="instantly">Instantly</p>
    <p class="safe">SAFE</p>
    <p class="audience">for people<br>and pets</p>

    <svg class="no-chemicals" viewBox="660 60 520 420" aria-label="Chemicals crossed out">
      <circle cx="914" cy="262" r="196" fill="var(--paper)"/>
      <circle cx="914" cy="262" r="184" fill="none" stroke="var(--stop-red)" stroke-width="18"/>
      <rect x="678" y="178" width="472" height="194" rx="14" fill="var(--paper)" stroke="var(--ink)" stroke-width="3"/>
      <text x="686" y="358" textLength="456" lengthAdjust="spacingAndGlyphs"
            font-family="Anton, sans-serif" font-size="218"
            fill="var(--ink)" stroke="var(--paper)" stroke-width="3" paint-order="stroke">CHEMICALS</text>
      <line x1="1050" y1="150" x2="786" y2="398" stroke="var(--paper)" stroke-width="26"/>
      <line x1="1050" y1="150" x2="786" y2="398" stroke="var(--stop-red)" stroke-width="18"/>
    </svg>

    <p class="contact">
      <span class="phone">615-555-0142</span><span class="web">meadowtrim.com</span>
    </p>
  </main>
</body>
</html>
```